National online rug retailer needs a home page design

See the MatsNowly logo and create a home page design around that color theme. Details are spelled out in word document uploaded below.

Apparently this website did not take my attachement showing the logo and basic requirements.  If you would send me your email address, I will send you the attachment directly.
Best regards,
Ned Ferris
nferris@qorvex.com

Target Market(s)

The target market is home owners 25 to 75 years old with combined incomes over $100,000 per year.

Industry/Entity Type

Online

Requirements
Must have
• Lots of white space with black letters and creative use of red and possibly one other color. Would like a compelling call to action button.

```html
<!DOCTYPE html>
<html lang="en">
<head>
<meta charset="utf-8">
<title>MatsNowly – Home</title>
<link href="https://fonts.googleapis.com/css2?family=Roboto:wght@400;500;700&display=swap" rel="stylesheet">
<style>
:root{
  --red:#d51a1f;--red-dark:#b5121a;--ink:#222;--text:#555;--muted:#777;
  --bar:#2b2b2b;--page:#f2f2f2;--line:#e2e2e2;--panel:#8d8d8d;--green:#2e9a1e;
}
*{box-sizing:border-box;margin:0;padding:0}
html,body{width:789px;height:1200px;overflow:hidden}
body{font-family:"Roboto",Arial,sans-serif;background:var(--page);color:var(--text);position:relative;font-size:9px}
.abs{position:absolute}
.topbar{left:0;top:0;width:789px;height:32px;background:var(--bar);color:#fff;font-size:9px}
.topbar .links{position:absolute;right:59px;top:10px;display:flex;gap:8px}
.logo{left:61px;top:44px;font-size:30px;color:var(--red);font-weight:500;display:flex;align-items:center;gap:6px}
.logo .sq{width:12px;height:12px;background:var(--red)}
.tagline{left:118px;top:81px;font-size:7px;color:var(--muted)}
.search{left:292px;top:63px;display:flex}
.search .field{width:150px;height:26px;border:1px solid #ccc;background:#fff;font-size:8px;color:#999;padding:8px}
.search .go{width:55px;height:26px;background:#666;color:#fff;font-size:9px;font-weight:500;display:flex;align-items:center;justify-content:center}
.phone{right:59px;top:45px;font-size:13px;font-weight:700;color:#666}
.phone b{color:var(--red)}
.acct{right:59px;top:64px;display:flex;gap:3px}
.acct span{height:24px;padding:0 8px;background:#444;color:#fff;font-size:8.5px;font-weight:500;display:flex;align-items:center}
.acct .chat{background:var(--green);gap:5px}
.acct .chat i{width:10px;height:10px;border-radius:50%;background:#f5d322}
.nav{left:59px;top:102px;width:671px;height:33px;background:var(--red);display:flex;color:#fff;font-size:10px;font-weight:500}
.nav span{display:flex;align-items:center;padding:0 16px;border-right:1px solid var(--red-dark)}
.nav .home{background:#3a3a3a;padding:0 20px}
.main{left:59px;top:141px;width:671px;height:795px;background:#fff}
.browse{left:70px;top:151px;font-size:13px;font-weight:700;color:var(--red)}
.theme{left:70px;top:173px;width:164px;height:28px;background:var(--red);color:#fff;font-size:10px;font-weight:500;display:flex;align-items:center;padding-left:12px;gap:8px}
.minus,.plus{width:10px;height:10px;border-radius:50%;background:#fff;position:relative}
.plus{background:#aaa}
.minus::after,.plus::after{content:"";position:absolute;left:2px;top:4px;width:6px;height:2px;background:var(--red)}
.plus::after{background:#fff}
.plus::before{content:"";position:absolute;left:4px;top:2px;width:2px;height:6px;background:#fff}
.sub{left:100px;font-size:9.5px;color:#555}
.sub.on{color:var(--red)}
.facet{left:70px;width:164px;height:28px;background:#f4f4f4;border:1px solid #e6e6e6;font-size:9.5px;font-weight:500;color:#555;display:flex;align-items:center;padding-left:11px;gap:10px}
.about{left:70px;top:509px;width:164px;height:216px;background:#f4f4f4;padding:12px 11px}
.about h3{font-size:13px;color:var(--red);margin-bottom:8px}
.about p{font-size:8.3px;line-height:15.2px;text-align:justify;margin-bottom:5px}
.pay-lbl{left:79px;top:740px;font-size:9.5px;font-weight:500;color:#666}
.chips{left:79px;top:761px;display:flex;gap:5px}
.chips i{width:20px;height:12px;background:#ddd;border:1px solid #bbb}
.badge{background:#e9e9e9;border:1px solid #bbb}
.banner{left:252px;top:158px;width:463px;height:160px;background:linear-gradient(90deg,#4b5a60,#a8505a 40%,#c98a4a 70%,#6a7a6a)}
.arrows{left:673px;top:293px;display:flex;gap:3px}
.arrows i{width:16px;height:16px;border-radius:50%;background:#fff;border:2px solid #333}
.rugs-h{left:247px;top:340px;font-size:13px;font-weight:500;color:#333}
.panel{left:560px;top:332px;width:161px;height:600px;background:var(--panel)}
.panel h3{color:#fff;font-size:13px;font-weight:500;text-align:center;margin-top:8px}
.card{width:146px;height:176px;background:#fff;border:1px solid #e8e8e8;box-shadow:0 0 0 3px #f3f3f3;padding:6px 8px}
.card .img{width:132px;height:80px;margin-left:-1px}
.card .t{font-size:9.5px;color:#444;margin:12px 0 0 0}
.card .p{font-size:9.5px;color:var(--red);margin-top:8px}
.card .buy{margin-top:8px;width:120px;height:26px;background:linear-gradient(#8e8e8e,#6c6c6c);color:#fff;font-weight:500;font-size:9.5px;display:flex;align-items:center;justify-content:center;gap:5px}
.foot h4{font-size:11.5px;font-weight:400;color:#333;margin-bottom:6px}
.foot p{font-size:8px;color:#666;line-height:16.4px}
.fpay{left:341px;top:1032px;width:194px;height:107px;background:#fff;padding:10px 13px}
.fpay h4{font-size:11px;font-weight:400;color:#333;margin-bottom:12px}
.fpay .row{display:flex;gap:5px;margin-bottom:12px}
.fpay .row i{width:24px;height:13px;background:#ddd;border:1px solid #bbb}
.fpay .row.b i{width:26px;height:18px;border-radius:3px}
.social{left:584px;top:984px;display:flex;gap:9px}
.social i{width:18px;height:18px;background:#3c78b8;border-radius:2px}
.input{left:581px;width:149px;height:19px;background:#fff;border:1px solid #ccc;font-size:7.5px;color:#444;padding:5px 10px}
.submit{left:683px;top:1119px;width:47px;height:18px;background:#666;color:#fff;font-size:9px;font-weight:500;display:flex;align-items:center;justify-content:center}
.bottom{left:0;top:1160px;width:789px;height:40px;background:var(--bar);color:#bbb;font-size:8px;text-align:center;padding-top:15px}
.divider{left:557px;top:960px;width:1px;height:180px;background:#ccc}
</style>
</head>
<body>
<header>
  <div class="abs topbar"><div class="links"><span>ITEMS: ___</span><span>|</span><span>TOTAL $0.00</span><span>|</span><span>VIEW CART</span><span>|</span><span>CHECKOUT</span></div></div>
  <div class="abs logo"><span class="sq"></span>MatsNowly</div>
  <div class="abs tagline">for domestic and heirloom values</div>
  <div class="abs search"><div class="field">Enter key words or item #</div><div class="go">SEARCH</div></div>
  <div class="abs phone">ORDER TOLL-FREE : <b>1-888-555-0142</b></div>
  <div class="abs acct"><span>MY ACCOUNT</span><span>SIGN IN</span><span class="chat"><i></i>LIVE CHAT</span></div>
  <nav class="abs nav"><span class="home">HOME</span><span>SELECTION GUIDES</span><span>RUG CARE</span><span>FAQ</span><span>RETURN POLICY</span><span>FREE SHIPPING</span><span style="border:0">CLEARANCE RUGS</span></nav>
</header>
<div class="abs main"></div>
<aside>
  <div class="abs browse">Browse</div>
  <div class="abs theme"><span class="minus"></span>RUG THEME</div>
  <div class="abs sub on" style="top:212px">» Traditional</div>
  <div class="abs sub" style="top:234px">» Transitional</div>
  <div class="abs sub" style="top:256px">» Casual</div>
  <div class="abs facet" style="top:278px"><span class="plus"></span>COLOR WAY</div>
  <div class="abs facet" style="top:310px"><span class="plus"></span>SIZE</div>
  <div class="abs facet" style="top:342px"><span class="plus"></span>SHAPE</div>
  <div class="abs facet" style="top:374px"><span class="plus"></span>FIBER CONTENT</div>
  <div class="abs facet" style="top:406px"><span class="plus"></span>MFGR. BRAND</div>
  <div class="abs facet" style="top:438px"><span class="plus"></span>MFGR.COLLECTION</div>
  <div class="abs facet" style="top:470px"><span class="plus"></span>PRICE</div>
  <div class="abs about"><h3>About MatsNowly</h3>
    <p>Sed vitae augue felis. Fusce pulvinar sapien velit, eu varius nisl fringilla vel. Duis at tempus metus. Cras accumsan aliquet diam et egestas. Phasellus sit amet mi mi. Aenean interdum pretium tellus, vitae malesuada metus consequat ut.</p>
    <p>Suspendisse in cursus est. Suspendisse ultricies sed neque et etlanc adipiscing. Phasellus fermentum nec diam velit.</p></div>
  <div class="abs pay-lbl">Payments</div>
  <div class="abs chips"><i></i><i></i><i></i><i></i><i></i></div>
  <div class="abs badge" style="left:80px;top:790px;width:99px;height:32px"></div>
  <div class="abs badge" style="left:80px;top:830px;width:97px;height:43px;border-radius:6px"></div>
</aside>
<section>
  <div class="abs banner" role="img" aria-label="Summer sale banner: colourful felt-ball rug on a wooden floor, 20% offer"></div>
  <div class="abs arrows"><i></i><i></i></div>
  <div class="abs rugs-h">Rugs</div>
  <div class="abs panel"><h3>You may also like</h3></div>
  <div class="abs card" style="left:248px;top:364px"><div class="img" role="img" aria-label="Cream rug with dark patterned border" style="background:linear-gradient(135deg,#6a5548,#d8ccb4)"></div><div class="t">Traditional Rugs</div><div class="p">Price : $42.00 - $635.26</div><div class="buy">Buy Now</div></div>
  <div class="abs card" style="left:404px;top:364px"><div class="img" role="img" aria-label="Round navy shag rug on a tan floor" style="background:linear-gradient(135deg,#3a3c78,#8c7a8a)"></div><div class="t">Traditional Rugs</div><div class="p">Price : $42.00 - $635.26</div><div class="buy">Buy Now</div></div>
  <div class="abs card" style="left:567px;top:364px"><div class="img" role="img" aria-label="Cream rug with red floral pattern" style="background:linear-gradient(135deg,#e6d6c6,#c8687a)"></div><div class="t">Traditional Rugs</div><div class="p">Price : $42.00 - $635.26</div><div class="buy">Buy Now</div></div>
  <div class="abs card" style="left:248px;top:556px"><div class="img" role="img" aria-label="Red and brown medallion rug" style="background:linear-gradient(135deg,#d8c0b4,#8e3a2c)"></div><div class="t">Traditional Rugs</div><div class="p">Price : $42.00 - $635.26</div><div class="buy">Buy Now</div></div>
  <div class="abs card" style="left:404px;top:556px"><div class="img" role="img" aria-label="Red Bokhara pattern rug" style="background:#9c1f26"></div><div class="t">Traditional Rugs</div><div class="p">Price : $42.00 - $635.26</div><div class="buy">Buy Now</div></div>
  <div class="abs card" style="left:567px;top:556px"><div class="img" role="img" aria-label="Blue-grey shag rug" style="background:#6f8599"></div><div class="t">Traditional Rugs</div><div class="p">Price : $42.00 - $635.26</div><div class="buy">Buy Now</div></div>
  <div class="abs card" style="left:248px;top:748px"><div class="img" role="img" aria-label="Multicolour patchwork rug" style="background:linear-gradient(135deg,#6a2a1e,#a8704e)"></div><div class="t">Traditional Rugs</div><div class="p">Price : $42.00 - $635.26</div><div class="buy">Buy Now</div></div>
  <div class="abs card" style="left:404px;top:748px"><div class="img" role="img" aria-label="Red and green Persian rug on a floor" style="background:linear-gradient(135deg,#c8a67a,#7e3a2a)"></div><div class="t">Traditional Rugs</div><div class="p">Price : $42.00 - $635.26</div><div class="buy">Buy Now</div></div>
  <div class="abs card" style="left:567px;top:748px"><div class="img" role="img" aria-label="Natural jute rug on wooden floor" style="background:linear-gradient(#c9b390,#a57a52)"></div><div class="t">Traditional Rugs</div><div class="p">Price : $42.00 - $635.26</div><div class="buy">Buy Now</div></div>
</section>
<footer>
  <div class="abs foot" style="left:59px;top:960px"><h4>Customer Service</h4><p>Shipping<br>Return Policy<br>Privacy Policy<br>Ordering &amp; Delivery Checklist<br>Terms of Use<br>Terms of Sale<br>Contact Us<br>Environmental Policy</p></div>
  <div class="abs foot" style="left:217px;top:960px"><h4>Resources</h4><p>Product Articles<br>Learning Center<br>Help<br>Refer A Friend<br>MatsNowly Blog<br>Room Scene Viewer<br>Site Map<br>FAQ<br>Customer Testimonials<br>Photo Gallery</p></div>
  <div class="abs foot" style="left:341px;top:960px"><h4>Corporate Info</h4><p>About MatsNowly.com<br>Careers<br>Affiliates</p></div>
  <div class="abs fpay"><h4>Payments</h4><div class="row"><i></i><i></i><i></i><i></i><i></i><i></i></div><div class="row b"><i></i><i></i><i></i><i></i><i></i></div></div>
  <div class="abs divider"></div>
  <div class="abs foot" style="left:581px;top:960px"><h4>Connect with us</h4></div>
  <div class="abs social"><i></i><i></i><i></i></div>
  <div class="abs foot" style="left:581px;top:1040px"><h4>Email Signup</h4></div>
  <div class="abs input" style="top:1064px">Name</div>
  <div class="abs input" style="top:1092px">Email ID</div>
  <div class="abs submit">SUBMIT</div>
  <div class="abs bottom">Copyright © 2013 www.matsnowly.com All rights reserved.</div>
</footer>
</body>
</html>
```